mapleridgegroup Business Card Design

Business card with logo design for mapleridgegroup. We are a group of professional project managers based on the Pareto Principle that 80% of the work is done by 20% of the people. I have a makeshift logo that uses a pi chart with 30% and 20% and the 20% pie slice is set slightly out and up. Have played around with a teal and orange colour scheme.

Industry/Entity Type

Business

Contact Information for Business Card

Gareth Pembroke
Director
mapleridgegroup

0452 803716

```html
<!DOCTYPE html>
<html lang="en">
<head>
<meta charset="utf-8">
<title>Mapleridge Management — Business Card</title>
<link rel="stylesheet" href="https://fonts.googleapis.com/css2?family=Raleway:wght@200;300;400;600;700;800&display=swap">
<style>
  :root {
    --orange: #ee6a43;
    --teal: #2596a0;
    --ink: #4a4a4c;
    --ink-soft: #6e6e70;
    --paper: #ffffff;
    --backdrop: #8a8a8a;
    --rule: #cfcfcf;
  }
  * { margin: 0; padding: 0; box-sizing: border-box; }
  html, body { width: 1200px; height: 1000px; overflow: hidden; }
  body {
    font-family: "Raleway", sans-serif;
    background: var(--paper);
    color: var(--ink);
    position: relative;
  }

  .showcase {
    position: absolute; left: 0; top: 0;
    width: 1200px; height: 686px;
    background: var(--backdrop);
  }

  .card {
    position: absolute; left: 300px; top: 173px;
    width: 600px; height: 340px;
    background: var(--paper);
    overflow: hidden;
    box-shadow: 0 18px 40px rgba(0,0,0,.25);
  }
  .card__shapes { position: absolute; inset: 0; }

  .card__brand {
    position: absolute; left: 250px; top: 48px;
    display: flex; flex-direction: column; align-items: center;
    color: var(--paper);
  }
  .card__brand-dot {
    width: 44px; height: 44px; border-radius: 50%;
    background: var(--paper); margin-bottom: 12px;
  }
  .card__brand-name {
    font-weight: 700; font-size: 20px; line-height: 1.15;
    text-align: center; letter-spacing: .5px;
  }

  .card__corner-brand {
    position: absolute; right: 22px; top: 128px;
    display: flex; align-items: center; gap: 6px;
    font-weight: 700; font-size: 9px; color: var(--ink);
  }
  .card__corner-dot { width: 12px; height: 12px; border-radius: 50%; background: var(--orange); }

  .card__holder {
    position: absolute; left: 28px; top: 252px;
  }
  .card__name {
    font-weight: 800; font-size: 20px; letter-spacing: .6px;
    text-transform: uppercase; color: var(--ink);
  }
  .card__role { font-weight: 400; font-size: 11px; color: var(--ink-soft); margin-top: 2px; }

  .card__contact {
    position: absolute; left: 28px; right: 28px; top: 304px;
    border-top: 1px solid var(--rule);
    padding-top: 8px;
    display: flex; gap: 10px; align-items: center;
    font-size: 10.5px; font-weight: 400; color: var(--ink-soft);
  }
  .card__sep { width: 6px; height: 6px; border-radius: 50%; border: 1.5px solid var(--ink-soft); }

  .logo-set {
    position: absolute; top: 756px; width: 260px;
    display: flex; flex-direction: column; align-items: center;
  }
  .logo-set--mono { left: 200px; }
  .logo-set--colour { left: 732px; }
  .logo-set__dot { width: 90px; height: 90px; border-radius: 50%; }
  .logo-set--mono .logo-set__dot { background: var(--ink); }
  .logo-set--colour .logo-set__dot { background: var(--orange); }
  .logo-set__name {
    margin-top: 24px;
    font-weight: 700; font-size: 31px; line-height: 1.15;
    color: var(--ink); text-align: center; letter-spacing: .5px;
  }
</style>
</head>
<body>
  <section class="showcase">
    <article class="card">
      <svg class="card__shapes" width="600" height="340" viewBox="0 0 600 340" aria-hidden="true">
        <polygon points="0,0 600,0 600,110 0,240" fill="var(--orange)"/>
        <polygon points="360,0 600,0 600,110 420,149" fill="var(--teal)"/>
      </svg>

      <div class="card__brand">
        <div class="card__brand-dot"></div>
        <div class="card__brand-name">Mapleridge<br>Management</div>
      </div>

      <div class="card__corner-brand">
        <span class="card__corner-dot"></span>
        <span>Mapleridge Management</span>
      </div>

      <div class="card__holder">
        <h1 class="card__name">Gareth Pembroke</h1>
        <p class="card__role">Director mapleridgegroup</p>
      </div>

      <p class="card__contact">
        <span>address str Name 25</span>
        <span class="card__sep"></span>
        <span>tel: 0452 803716</span>
        <span class="card__sep"></span>
        <span>e-mail: hello@mapleridgegroup.com</span>
      </p>
    </article>
  </section>

  <div class="logo-set logo-set--mono">
    <div class="logo-set__dot"></div>
    <p class="logo-set__name">Mapleridge<br>Management</p>
  </div>

  <div class="logo-set logo-set--colour">
    <div class="logo-set__dot"></div>
    <p class="logo-set__name">Mapleridge<br>Management</p>
  </div>
</body>
</html>
```